Real Estate Website

We need a web design for a new site that is focused on real estate listings and information for the Singapore, Malaysian and Australian market.

The web site will have listings of available real estate for sale, past transaction data on real estate, information about neighborhoods where the real estate is located.
Website URL will likely be www.havenlotz.com. We are also open to suggestions on site names (assuming URL is available).

We like the simplicity of a similar US site called Pevondo.com - and want to focus on providing a similar "clean" user interface where users can find the information they need. The final design should be user friendly, be visually compelling with a focus on ease of navigation.

Requirements to have at least 5 web pages designed that will display the data as in the attached document for any given territory. We will need to receive
- HTML/CSS/JavaScript, and all images
- any design icons for common objects (e.g. house/home, map, user, agent, trend chart, contact, bathroom, bedroom, garage, furniture, price, ...etc).
Updates

Hi

I just added more details to the brief and committed to pay for the project.
Please review the additional information and submit your final designs by June 14th (or sooner) as we have a deadline to meet. 

Let me know if you have any questions, I will try to be prompt in my responses. 
Thanks.

Target Market(s)

Consumers who are researching real estate to purchase or sell

Industry/Entity Type

Real Estate

Requirements
Must have
• Data in attached document needs to be displayed.

```html
<!DOCTYPE html>
<html lang="en">
<head>
<meta charset="utf-8">
<title>Real Estate – Your Best Real Estate Agent</title>
<link rel="stylesheet" href="https://fonts.googleapis.com/css2?family=Arimo:wght@400;700&display=swap">
<style>
  :root{
    --navy-dark:#0c3559;
    --navy:#164c78;
    --panel-blue:#1f5f92;
    --panel-blue-deep:#184f7c;
    --teal-line:#5bb5dc;
    --field:#123f66;
    --field-border:#2f6f9f;
    --paper:#f4f4f2;
    --paper-edge:#e3e3e0;
    --ink:#333333;
    --ink-strong:#1d1d1d;
    --heading-blue:#1f3b57;
    --orange:#f08a12;
    --green:#5a8f10;
    --green-bright:#7fb51c;
    --link-yellow:#ffde3a;
    --white:#ffffff;
  }
  *{box-sizing:border-box;margin:0;padding:0}
  html,body{width:1164px;height:1200px;overflow:hidden;background:var(--navy-dark)}
  body{font-family:"Arimo",Arial,sans-serif;color:var(--ink)}
  .page{position:absolute;left:0;top:0;width:766px;height:790px;transform:scale(1.5196,1.519);transform-origin:0 0;
    background:linear-gradient(180deg,var(--navy) 0,var(--navy-dark) 100%);overflow:hidden}
  .abs{position:absolute}

  /* header */
  .site-header{left:0;top:0;width:766px;height:75px;background:linear-gradient(180deg,#123e65 0,#0e3457 100%);border-bottom:1px solid #0a2a47}
  .brand-dot{left:22px;top:16px;width:32px;height:32px;border-radius:50%;background:var(--green-bright)}
  .brand-name{left:78px;top:17px;font-size:27px;font-weight:700;color:#e6edf3;letter-spacing:.2px;line-height:27px;white-space:nowrap}
  .brand-tagline{left:79px;top:44px;font-size:8.5px;line-height:10px;color:#7faccd;letter-spacing:.2px;white-space:nowrap}
  .utility-nav{left:569px;top:28px;display:flex;gap:20px;font-size:10px;color:#dfe9f2}
  .utility-nav span{display:flex;align-items:center;gap:6px}
  .utility-nav i{display:block;width:10px;height:10px;background:var(--green-bright);border:2px solid #3f6e1b}

  /* hero */
  .hero-photo{left:0;top:75px;width:536px;height:261px;
    background:linear-gradient(180deg,#5aa3e0 0,#a9d3f0 35%,#7e9a6a 60%,#4f8d2c 80%,#6f7378 100%);
    clip-path:polygon(0 0,100% 0,100% 86%,96% 100%,0 100%)}
  .call-box{left:0;top:311px;width:200px;height:43px;background:var(--white);display:flex;align-items:center;gap:20px;padding-left:8px;font-size:11px;z-index:3;white-space:nowrap}
  .call-box b{color:var(--green)}
  .call-box em{font-style:normal;color:var(--navy)}

  /* main nav */
  .main-nav{left:537px;top:75px;width:229px;height:188px;background:linear-gradient(180deg,#49acd6 0,#3391bf 100%)}
  .main-nav ul{list-style:none;padding-top:16px}
  .main-nav li{height:26px;line-height:26px;text-align:right;padding-right:40px;font-size:11.5px;font-weight:700;color:var(--white);letter-spacing:.6px;border-bottom:1px solid var(--teal-line)}

  /* search panel */
  .search-panel{left:524px;top:263px;width:242px;height:435px;background:linear-gradient(180deg,var(--panel-blue) 0,var(--panel-blue-deep) 100%)}
  .search-title{left:568px;top:300px;display:flex;align-items:center;gap:14px}
  .search-title h2{font-size:16px;font-weight:700;color:var(--white);line-height:1;letter-spacing:.3px}
  .search-title h2 small{font-size:12px}
  .search-form{left:559px;top:372px;width:187px;font-size:11px;color:var(--white)}
  .search-form label{display:block;font-weight:700;margin-bottom:3px;white-space:nowrap}
  .field{height:18px;background:var(--field);border:1px solid var(--field-border);margin-bottom:12px;position:relative;font-size:9px;color:#7b9dbb;line-height:16px;padding-left:5px}
  .field.select::after{content:"";position:absolute;right:0;top:0;width:16px;height:16px;background:var(--field);border-left:1px solid var(--field-border)}
  .field.select::before{content:"";position:absolute;right:4px;top:6px;border:4px solid transparent;border-top-color:#8fc3e8;z-index:1}
  .range{display:flex;gap:13px}
  .range .field{width:87px}
  .range-labels{display:flex;gap:47px}
  .search-btn{left:673px;top:601px;width:73px;height:20px;background:linear-gradient(180deg,#67c6ef 0,#2c8fc7 100%);color:var(--white);font-size:11px;font-weight:700;text-align:center;line-height:18px;border:1px solid #7bd0f2}
  .advanced{left:563px;top:639px;font-size:10.5px;color:#e3eef7;line-height:14px;white-space:nowrap}
  .advanced a{color:var(--link-yellow);text-decoration:underline}

  /* content */
  .content{left:0;top:336px;width:521px;height:390px;background:linear-gradient(90deg,var(--paper-edge) 0,var(--paper) 20%,var(--paper) 100%);
    clip-path:polygon(0 0,100% 0,100% 90%,95% 100%,0 100%)}
  .photo-stack{left:22px;top:388px;width:132px;height:112px;transform:rotate(-12deg);border:5px solid var(--white);
    background:linear-gradient(180deg,#6fa8d8 0,#d8d4c6 45%,#3f8b3c 75%,#3aa0c8 100%);box-shadow:2px 3px 6px rgba(0,0,0,.35)}
  .welcome{left:198px;top:395px;white-space:nowrap}
  .welcome h1{font-size:19px;font-weight:700;color:var(--orange);line-height:1}
  .welcome p{font-size:12px;color:#a0a0a0;margin-top:1px}
  .intro{left:201px;top:435px;width:294px;font-size:10.3px;line-height:14.2px;color:var(--ink)}
  .intro b{color:var(--ink-strong)}
  .intro u,.services u{text-decoration:underline}
  .read-more{left:420px;top:518px;font-size:11px;font-weight:700;color:var(--ink-strong);display:flex;align-items:center;gap:5px;white-space:nowrap}
  .services{left:42px;top:561px;width:460px}
  .services h2{font-size:12.5px;font-weight:700;color:var(--heading-blue);letter-spacing:.4px}
  .services h3{font-size:11px;font-weight:700;color:var(--ink-strong);margin-top:14px;white-space:nowrap}
  .services p{font-size:10.3px;line-height:14.2px;margin-top:3px}
  .service-links{left:42px;top:658px;display:grid;grid-template-columns:230px 230px;row-gap:5px;font-size:10.5px;white-space:nowrap}
  .service-links a{color:var(--green);display:flex;align-items:center;gap:10px}
  .service-links a span{text-decoration:underline}
  .service-links a::before{content:"";width:0;height:0;border:4px solid transparent;border-left:6px solid var(--green-bright);border-right:0}

  /* footer */
  .site-footer{left:0;top:726px;width:766px;height:64px;background:linear-gradient(180deg,#123f67 0,#0e3456 100%)}
  .footer-nav{left:42px;top:753px;display:flex;gap:10px;font-size:10.5px;color:#c9d8e6;white-space:nowrap}
  .footer-nav i{font-style:normal;color:#6f93b3}
  .copyright{right:24px;top:737px;font-size:10.5px;color:#c9d8e6;line-height:14px;text-align:right;white-space:nowrap}
  .copyright a{color:var(--orange);text-decoration:underline}
</style>
</head>
<body>
<div class="page">
  <header class="site-header abs"></header>
  <span class="brand-dot abs"></span>
  <div class="brand-name abs">REAL ESTATE</div>
  <div class="brand-tagline abs">YOUR BEST REAL ESTATE AGENT</div>
  <nav class="utility-nav abs"><span><i></i>home</span><span><i></i>search</span><span><i></i>help</span></nav>

  <div class="hero-photo abs" role="img" aria-label="Photo of a large white suburban house with lawn, trees and a curving street under a blue sky"></div>
  <div class="call-box abs">
    <svg width="20" height="20" viewBox="0 0 20 20" aria-hidden="true"><path d="M4 2 L8 6 L6 8 C7 11 9 13 12 14 L14 12 L18 16 L15 19 C8 18 2 12 1 5 Z" fill="#333"/></svg>
    <span><b>Call Now:</b> <em>1-800-555-0148</em></span>
  </div>

  <nav class="main-nav abs"><ul><li>BUYING</li><li>BUILDING</li><li>SELLING</li><li>MOVING</li><li>INSURANCE</li><li>CONTACTS</li></ul></nav>

  <aside class="search-panel abs"></aside>
  <div class="search-title abs">
    <svg width="34" height="36" viewBox="0 0 34 36" aria-hidden="true"><circle cx="20" cy="13" r="10" fill="#bfe3f5" stroke="#eef6fb" stroke-width="3"/><path d="M12 21 L3 31" stroke="#f08a12" stroke-width="5" stroke-linecap="round"/></svg>
    <h2>FIND <small>YOUR</small><br>PROPERTY</h2>
  </div>
  <form class="search-form abs">
    <label>City &amp; State, or Zip:</label><div class="field"></div>
    <label>Search Area</label><div class="field select">no radius</div>
    <div class="range-labels"><label>Price Range</label><label>to</label></div>
    <div class="range"><div class="field select">all prices</div><div class="field select">all prices</div></div>
    <label>Bedroom(s)</label><div class="field select">any number</div>
    <label>Bathroom(s)</label><div class="field select">any number</div>
  </form>
  <div class="search-btn abs">Search</div>
  <div class="advanced abs">Know exactly what you want? Try our<br><a>Advanced search</a></div>

  <main class="content abs"></main>
  <div class="photo-stack abs" role="img" aria-label="Stack of property photos showing a house with a swimming pool"></div>
  <div class="welcome abs"><h1>WELCOME</h1><p>to our real estate website!</p></div>
  <p class="intro abs"><b>Lorem ipsum dolor</b> sit amet, consectetur isig elit, sed do <u>eiusmod tempor</u> incididunt ut labore et dolore magna aliqua. Ut enim ad minim veniam, quis nostrud exercitation ullamco laboris nisi ut aliquip ex ea commodo consequat. Duis aute re dolor in reprehenderit in voluptate velit.</p>
  <div class="read-more abs"><svg width="9" height="8" viewBox="0 0 9 8" aria-hidden="true"><path d="M0 2.5h4V0l5 4-5 4V5.5H0z" fill="#f08a12"/></svg>read more</div>
  <section class="services abs">
    <h2>FEATURED SERVICES</h2>
    <h3>Lorem ipsum dolor sit amet, consectetur isig elit</h3>
    <p>Sed do <u>eiusmod tempor</u> incididunt ut labore et dolore magna aliqua. Ut enim ad minim veniam, quis nostrud exercitation ullamco laboris nisi ut aliquip ex ea commodo consequat.</p>
  </section>
  <div class="service-links abs">
    <a><span>Ut labore et dolore magna aliqua</span></a><a><span>Ut labore et dolore magna aliqua</span></a>
    <a><span>Enim ad minim veniam.</span></a><a><span>Enim ad minim veniam.</span></a>
  </div>

  <footer class="site-footer abs"></footer>
  <nav class="footer-nav abs"><span>Home</span><i>:</i><span>Building</span><i>:</i><span>Buying</span><i>:</i><span>Selling</span><i>:</i><span>Moving</span><i>:</i><span>Insurance</span><i>:</i><span>Contacts</span></nav>
  <div class="copyright abs">Real Estate © 2012<br><a>Privacy Policy</a></div>
</div>
</body>
</html>
```